Homepage design for female-owned English/French speaking Law firm

Brief Update - we prefer not to have a photo of a person in the hero shot

Corvell.com.au is the website for a English/French Bilingual Female-owned Law Firm, Morillaqua Corvell.
Overall Design notes:
Professional, yet warm and welcoming
Historic foundations but Progressive, woman-owned, sleek, innovative and modern.
Approachable, casual yet professional. Sans-serif font and light colours would help this
2 languages switched by flags (English/French)

Winner must provide
Home page design
Standard (inner) page design (can be provided after winner is selected)
All photos used in the design without charge
Updates

Requirements
Should not have
• Update - we prefer not to have a photo of a person in the hero shot

```html
<!DOCTYPE html>
<html lang="en">
<head>
<meta charset="utf-8">
<title>Morillaqua Corvell Solicitors</title>
<link href="https://fonts.googleapis.com/css2?family=Poppins:wght@300;400;500;600;700&display=swap" rel="stylesheet">
<style>
:root{
  --orange:#f7902f;
  --orange-dark:#e97e1c;
  --ink:#1d1d1d;
  --text:#555;
  --muted:#8a8a8a;
  --cream:#fdf3e9;
  --cream-deep:#fde8d3;
  --line:#f1dcc6;
  --dark:#2b2b2b;
  --white:#fff;
}
*{box-sizing:border-box;margin:0;padding:0}
html,body{width:1200px;height:4633px;overflow:hidden}
body{font-family:'Poppins',sans-serif;color:var(--ink);background:var(--white);position:relative}
.abs{position:absolute}
a{color:inherit;text-decoration:none}

/* header */
.site-header{position:absolute;left:0;top:0;width:1200px;height:135px;background:var(--white)}
.brand{position:absolute;left:75px;top:44px;display:flex;align-items:center;gap:12px}
.brand-mark{width:34px;height:34px;background:var(--orange);flex:0 0 34px}
.brand-name{font-size:22px;font-weight:600;color:var(--ink);line-height:1}
.brand-tag{font-size:11px;color:var(--muted);margin-top:5px}
.pill{position:absolute;top:36px;height:32px;border-radius:16px;background:var(--orange);color:#fff;font-size:12px;display:flex;align-items:center;padding:0 14px 0 4px;gap:10px}
.pill .dot{width:26px;height:26px;border-radius:50%;background:#fff;display:flex;align-items:center;justify-content:center}
.lang{position:absolute;left:1044px;top:42px;font-size:15px;display:flex;align-items:center;gap:6px}
.flag{width:24px;height:24px;border-radius:50%;background:linear-gradient(135deg,#23407a 0 40%,#d62d3a 40% 60%,#23407a 60%)}
.main-nav{position:absolute;top:86px;left:578px;display:flex;font-size:13px;color:#444}
.main-nav a{padding:0 13px 10px}
.main-nav a.active{color:var(--orange);border-bottom:2px solid var(--orange)}

/* hero */
.hero{position:absolute;left:0;top:135px;width:1200px;height:741px;background:linear-gradient(100deg,#3a2519 0%,#6b4630 35%,#a57a58 62%,#7a5438 80%,#3f2a1d 100%)}
.hero-title{position:absolute;left:72px;top:162px;font-size:66px;font-weight:500;color:#fff;line-height:75px}
.hero-title span{color:var(--orange)}
.hero-text{position:absolute;left:76px;top:328px;width:560px;font-size:14px;font-weight:500;line-height:24px;color:#fff}
.btn{display:inline-flex;align-items:center;justify-content:center;background:var(--orange);color:#fff;border-radius:30px;font-weight:500;text-transform:uppercase}
.hero .btn{position:absolute;left:76px;top:431px;width:194px;height:58px;font-size:17px}

/* features */
.features{position:absolute;left:75px;top:768px;width:1051px;height:187px;background:#fff;border-radius:22px;box-shadow:0 6px 24px rgba(0,0,0,.12);display:flex;overflow:hidden}
.feature{flex:1;display:flex;gap:16px;padding:36px 20px 0 28px}
.feature.hl{background:var(--orange);color:#fff;flex:0 0 337px;padding:36px 16px 0 12px}
.f-icon{flex:0 0 66px;height:66px;border-radius:50%;background:var(--orange);display:flex;align-items:center;justify-content:center;border:4px solid #fde3c9}
.feature.hl .f-icon{background:#fff;border-color:#ffcf9f}
.feature h3{font-size:16px;font-weight:600;margin-top:4px}
.feature p{font-size:11px;line-height:20px;color:var(--text);margin-top:6px}
.feature.hl p{color:#fff}

/* headings */
.eyebrow{font-size:22px;color:var(--orange);font-weight:400}
.title{font-size:50px;font-weight:600;line-height:1.05}
.center{text-align:center;width:1200px;left:0}

/* about */
.about-frame{left:100px;top:1171px;width:324px;height:340px;background:var(--orange)}
.about-photo{left:118px;top:1184px;width:370px;height:354px;background:linear-gradient(180deg,#6aa6e0 0%,#bcd6ef 45%,#7d9a5e 65%,#8a7f70 100%)}
.about-copy{left:570px;top:1168px;width:530px;font-size:13px;line-height:27px;color:var(--text);text-align:justify}
.about-copy p+p{margin-top:27px}

/* services */
.services{position:absolute;left:0;top:1655px;width:1200px;height:660px;background:var(--cream)}
.grid{position:absolute;left:75px;top:221px;width:1051px;display:grid;grid-template-columns:repeat(4,253px);column-gap:13px;row-gap:18px}
.svc{height:153px;background:#fff;border:1px solid var(--line);padding:22px 14px 0 16px;display:flex;gap:12px}
.s-icon{flex:0 0 52px;height:52px;border-radius:50%;background:var(--orange);border:3px solid #fde3c9;display:flex;align-items:center;justify-content:center}
.svc h3{font-size:14.5px;font-weight:500;color:var(--orange)}
.svc p{font-size:9px;line-height:15.5px;color:var(--text);margin-top:4px}
.svc .more{display:block;font-size:8px;font-weight:600;margin-top:8px;color:var(--ink)}
.svc .more.o{color:var(--orange);text-decoration:underline}

/* testimonials */
.avatar{left:243px;top:2533px;width:122px;height:122px;border-radius:50%;background:linear-gradient(160deg,#e4e4e4,#b9b9b9)}
.t-name{left:390px;top:2562px;font-size:15px;font-weight:600}
.t-role{left:390px;top:2584px;font-size:12px;color:var(--muted)}
.stars{left:390px;top:2608px;display:flex;gap:3px}
.t-photo{left:595px;top:2533px;width:369px;height:369px;border-radius:50%;background:radial-gradient(circle at 55% 55%,#b07a43 0%,#6b4a32 30%,#3a3a3a 60%,#2a2a2a 100%)}
.quote{left:236px;top:2671px;width:439px;height:290px;background:var(--orange);border-radius:30px;color:#fff;padding:40px 34px}
.quote p{font-size:12.5px;line-height:22.5px;margin-top:18px}
.arrow{width:48px;height:48px;border-radius:50%;display:flex;align-items:center;justify-content:center;top:2718px}
.arrow.prev{left:118px;background:#fff;box-shadow:0 2px 10px rgba(0,0,0,.15)}
.arrow.next{left:1034px;background:#3a3a3a}

/* blog */
.blog-bg{left:0;top:3046px;width:1200px;height:1038px;background:var(--cream)}
.post{top:3262px;width:280px}
.post .img{width:280px;height:176px;border-right:4px solid var(--orange);border-bottom:4px solid var(--orange)}
.post .date{font-size:11px;color:#666;margin-top:32px;display:flex;align-items:center;gap:8px}
.post h3{font-size:14.5px;font-weight:500;line-height:21px;margin-top:8px}
.post .more{font-size:9.5px;font-weight:600;color:var(--orange);text-decoration:underline;display:block;margin-top:9px}

/* contact */
.dark-band{left:0;top:4084px;width:1200px;height:549px;background:var(--dark)}
.contact-box{left:137px;top:3751px;width:914px;height:527px;background:var(--cream-deep)}
.field{font-size:13px;color:#888;border-bottom:1px solid #bbb;height:34px;display:flex;align-items:center;gap:10px;padding-left:4px}
.contact-frame{left:671px;top:3871px;width:318px;height:318px;background:var(--orange)}
.contact-photo{left:653px;top:3845px;width:318px;height:329px;background:radial-gradient(circle at 45% 45%,#8a5a36 0%,#4d3627 28%,#d9d9d9 55%,#f2f2f2 100%)}

/* footer */
.foot-logo{left:137px;top:4361px;width:356px;height:81px;border:2px solid #fff;background:var(--dark);padding:14px 18px;display:flex;align-items:center;gap:12px}
.foot-logo .brand-name{font-size:21px;color:#fff}
.foot-logo .brand-tag{font-size:10.5px;color:#ccc}
.social{left:248px;top:4472px;display:flex;gap:9px}
.social span{width:26px;height:26px;background:var(--orange);border-radius:3px}
.foot-h{font-size:22px;font-weight:500;color:#fff}
.foot-h::after{content:"";display:block;width:48px;height:2px;background:var(--orange);margin-top:8px}
.qlinks{list-style:none;font-size:13px;color:#fff}
.qlinks li{display:flex;align-items:center;gap:12px;height:27px}
.qlinks li::before{content:"";width:7px;height:7px;border-radius:50%;background:var(--orange)}
.c-item{display:flex;gap:22px;color:#fff;font-size:12.5px;line-height:16px}
.c-icon{flex:0 0 24px;height:24px;background:var(--orange);border-radius:4px;display:flex;align-items:center;justify-content:center}
.copy-line{left:0;top:4584px;width:1200px;border-top:1px solid #444}
.copyright{left:0;width:1200px;top:4600px;text-align:center;font-size:11.5px;color:#fff}
</style>
</head>
<body>

<header class="site-header">
  <div class="brand">
    <span class="brand-mark"></span>
    <div>
      <div class="brand-name">Morillaqua Corvell</div>
      <div class="brand-tag">Bilingual Legal Practice · Sydney</div>
    </div>
  </div>
  <div class="pill" style="left:648px">
    <span class="dot"><svg width="14" height="14" viewBox="0 0 24 24"><path fill="#f7902f" d="M6.6 10.8a15 15 0 006.6 6.6l2.2-2.2c.3-.3.7-.4 1-.2 1.1.4 2.3.6 3.6.6.6 0 1 .4 1 1V20c0 .6-.4 1-1 1A17 17 0 013 4c0-.6.4-1 1-1h3.5c.6 0 1 .4 1 1 0 1.3.2 2.5.6 3.6.1.3 0 .7-.2 1z"/></svg></span>
    (+612) 9555 0142
  </div>
  <div class="pill" style="left:812px">
    <span class="dot"><svg width="14" height="14" viewBox="0 0 24 24"><path fill="#f7902f" d="M3 5h18v14H3z"/><path fill="none" stroke="#fff" stroke-width="2" d="M3 6l9 7 9-7"/></svg></span>
    elise@corvell.com.au
  </div>
  <div class="lang">Eng <span class="flag" role="img" aria-label="English flag"></span><svg width="10" height="8" viewBox="0 0 10 8"><path d="M0 0h10L5 8z" fill="#222"/></svg></div>
  <nav class="main-nav">
    <a class="active" href="#">Home</a><a href="#">About Us</a><a href="#">Our Services ▾</a><a href="#">Download</a><a href="#">Contact Us</a><a href="#">Links</a>
  </nav>
</header>

<section class="hero" role="img" aria-label="Hand signing a document with a wooden fountain pen">
  <h1 class="hero-title">Welcome <span>morillaqua<br>corvell solicitors</span></h1>
  <p class="hero-text">We are a firm of French-speaking lawyers located in the Sydney central business district. We provide a broad range of legal services in English and French to clients in Australia and overseas.</p>
  <a class="btn" href="#">Know More</a>
</section>

<div class="features">
  <div class="feature">
    <div class="f-icon"><svg width="30" height="30" viewBox="0 0 24 24" fill="none" stroke="#fff" stroke-width="1.6"><rect x="3" y="4" width="18" height="13"/><path d="M7 9h10M7 12h6M9 21h6M12 17v4"/></svg></div>
    <div><h3>100% Success Rate</h3><p>Lorem ipsum dolor sit amet, consec tetur adipisci elit, sed eiusmod mpor incidunt ut labore et dolore magna aliqua. quis nostrum.</p></div>
  </div>
  <div class="feature hl">
    <div class="f-icon"><svg width="30" height="30" viewBox="0 0 24 24" fill="none" stroke="#f7902f" stroke-width="1.6"><circle cx="12" cy="9" r="4"/><path d="M4 20c1-4 4-6 8-6s7 2 8 6"/></svg></div>
    <div><h3>Expert Legal Services</h3><p>Lorem ipsum dolor sit amet, consec tetur adipisci elit, sed eiusmod mpor incidunt ut labore et dolore magna aliqua. quis nostrum.</p></div>
  </div>
  <div class="feature">
    <div class="f-icon"><svg width="30" height="30" viewBox="0 0 24 24" fill="none" stroke="#fff" stroke-width="1.6"><path d="M12 3l2.5 5 5.5.8-4 3.9.9 5.5L12 15.6 7.1 18.2 8 12.7 4 8.8 9.5 8z"/></svg></div>
    <div><h3>Highly Recommend</h3><p>Lorem ipsum dolor sit amet, consec tetur adipisci elit, sed eiusmod mpor incidunt ut labore et dolore magna aliqua. quis nostrum.</p></div>
  </div>
</div>

<!-- about -->
<div class="abs eyebrow" style="left:568px;top:1052px">Who We Are</div>
<h2 class="abs" style="left:568px;top:1080px;font-size:38px;font-weight:600">About Firm History</h2>
<div class="abs about-frame"></div>
<div class="abs about-photo" role="img" aria-label="Garden rotunda surrounded by palm trees under a blue sky"></div>
<div class="abs about-copy">
  <p>Morillaqua Corvell is a successor to the legal practice founded by Mr Lucien Armand Morillaqua in the 1930?s. Its various transformations saw Mr Lucien Armand Morillaqua and his sons work in partnership with other lawyers prior to forming a smaller family firm (Morillaqua &amp; Morillaqua) on their own. The firm name was changed to ?Morillaqua? when Pierre Morillaqua became sole proprietor of the firm in the early 1990?s.</p>
  <p>After working as an employed Solicitor with Pierre Morillaqua, Elise Corvell became proprietor of the firm in 1996 and the name of the practice was changed to?<br>Morillaqua Corvell?.</p>
</div>
<a class="abs btn" href="#" style="left:570px;top:1488px;width:173px;height:50px;font-size:16px">Read More</a>

<!-- services -->
<section class="services">
  <div class="abs eyebrow center" style="top:98px">Practice Areas</div>
  <h2 class="abs title center" style="top:124px">Our Services</h2>
  <div class="grid">
    <div class="svc"><div class="s-icon"><svg width="22" height="22" viewBox="0 0 24 24" fill="none" stroke="#fff" stroke-width="1.6"><path d="M3 11l9-7 9 7v9H3z"/></svg></div><div><h3>Property Law</h3><p>Our Property Law team has the legal knowledge and experience to make your purchase or sale of real estate as smooth as possible.</p><span class="more">READ MORE</span></div></div>
    <div class="svc"><div class="s-icon"><svg width="22" height="22" viewBox="0 0 24 24" fill="none" stroke="#fff" stroke-width="1.6"><rect x="5" y="3" width="14" height="18"/><path d="M8 8h8M8 12h8M8 16h5"/></svg></div><div><h3>Sale of Business</h3><p>If you are selling a business, it is important to contact us prior to entering a legally binding contract.</p><span class="more o">READ MORE</span></div></div>
    <div class="svc"><div class="s-icon"><svg width="22" height="22" viewBox="0 0 24 24" fill="none" stroke="#fff" stroke-width="1.6"><circle cx="12" cy="12" r="8"/><path d="M12 7v5l3 2"/></svg></div><div><h3>Wills &amp; Estates</h3><p>Estate Planning includes making a Will, making a Power of Attorney and appointing an Enduring Guardian.</p><span class="more">READ MORE</span></div></div>
    <div class="svc"><div class="s-icon"><svg width="22" height="22" viewBox="0 0 24 24" fill="none" stroke="#fff" stroke-width="1.6"><rect x="4" y="3" width="12" height="16"/><path d="M8 21h12V7"/></svg></div><div><h3>Translation Services</h3><p>Specialised translation of legal documents from French into English or from English into French including:</p><span class="more">READ MORE</span></div></div>
    <div class="svc"><div class="s-icon"><svg width="22" height="22" viewBox="0 0 24 24" fill="none" stroke="#fff" stroke-width="1.6"><circle cx="9" cy="8" r="3"/><circle cx="16" cy="9" r="2.5"/><path d="M3 20c0-4 3-6 6-6s6 2 6 6M15 14c3 0 6 2 6 6"/></svg></div><div><h3>Elder Law</h3><p>The definition of Retirement Village in the relevant legislation specifically excludes Aged Care Facilities.</p><span class="more">READ MORE</span></div></div>
    <div class="svc"><div class="s-icon"><svg width="22" height="22" viewBox="0 0 24 24" fill="none" stroke="#fff" stroke-width="1.6"><rect x="5" y="3" width="14" height="18"/><path d="M8 15l3 3 5-6"/></svg></div><div><h3>Power of Attorney</h3><p>We can assist you plan for the future by preparing a Power of Attorney and/or an Appointment of Enduring Guardian.</p><span class="more">READ MORE</span></div></div>
    <div class="svc"><div class="s-icon"><svg width="22" height="22" viewBox="0 0 24 24" fill="none" stroke="#fff" stroke-width="1.6"><rect x="5" y="3" width="14" height="18"/><path d="M8 8h8M8 12h8"/></svg></div><div><h3>French Advice</h3><p>Property transactions in France, New Caledonia or other French-speaking countries.</p><span class="more">READ MORE</span></div></div>
    <div class="svc"><div class="s-icon"><svg width="22" height="22" viewBox="0 0 24 24" fill="none" stroke="#fff" stroke-width="1.6"><path d="M4 20l8-8M10 6l8 8M13 3l8 8"/></svg></div><div><h3>Affairs Management</h3><p>We provide a number of services in addition to our legal services including Affairs Management.</p><span class="more">READ MORE</span></div></div>
  </div>
</section>

<!-- testimonials -->
<div class="abs eyebrow center" style="top:2400px">Reviews</div>
<h2 class="abs title center" style="top:2426px">Our Testimonials</h2>
<div class="abs t-photo" role="img" aria-label="Wooden judge's gavel on a desk"></div>
<div class="abs avatar" role="img" aria-label="Portrait of a client"></div>
<div class="abs t-name">Daniel Reyes</div>
<div class="abs t-role">Lorem ipsum</div>
<div class="abs stars">
  <svg width="86" height="16" viewBox="0 0 86 16"><g fill="#f7902f"><path id="st" d="M8 0l2.4 5 5.6.6-4.2 3.8 1.2 5.6L8 12.2 3 15l1.2-5.6L0 5.6 5.6 5z"/><use href="#st" x="17.5"/><use href="#st" x="35"/><use href="#st" x="52.5"/><use href="#st" x="70"/></g></svg>
</div>
<div class="abs quote">
  <svg width="40" height="30" viewBox="0 0 40 30"><path fill="#fff" d="M0 0h16v16l-6 14H3l5-14H0zM22 0h16v16l-6 14h-7l5-14h-8z"/></svg>
  <p>Lorem ipsum dolor sit amet, consectetur adipiscing elit. Sed vitae lobortis libero, at ultricies odio. Suspendisse vel sem in turpis tempus pretium. Etiam iaculis tortor sed egestas porttitor. Curabitur molestie pretium leo, quis sollicitudin nisi feugiat efficitur. Integer maximus elementum posuere tortor quis imperdiet.</p>
</div>
<div class="abs arrow prev"><svg width="18" height="14" viewBox="0 0 18 14"><path d="M17 7H2M7 1L1 7l6 6" fill="none" stroke="#222" stroke-width="2"/></svg></div>
<div class="abs arrow next"><svg width="18" height="14" viewBox="0 0 18 14"><path d="M1 7h15M11 1l6 6-6 6" fill="none" stroke="#fff" stroke-width="2"/></svg></div>

<!-- blog -->
<div class="abs blog-bg"></div>
<div class="abs eyebrow center" style="top:3132px">News &amp; Updates</div>
<h2 class="abs center" style="top:3158px;font-size:60px;font-weight:600;line-height:1.05">Our Blog</h2>
<article class="abs post" style="left:151px">
  <div class="img" role="img" aria-label="Gavel and scales beside hands exchanging money" style="background:linear-gradient(135deg,#f2ede6,#c9b79a 60%,#6a5a46)"></div>
  <div class="date"><svg width="14" height="14" viewBox="0 0 14 14" fill="none" stroke="#f7902f" stroke-width="1.4"><rect x="1" y="2" width="12" height="11"/><path d="M1 5h12M4 0v3M10 0v3"/></svg>May 10, 2023</div>
  <h3>Lorem ipsum dolor sit amet, con secte tur adipiscing elit</h3>
  <a class="more" href="#">READ MORE</a>
</article>
<article class="abs post" style="left:460px">
  <div class="img" role="img" aria-label="Two lawyers in conversation in an office" style="background:linear-gradient(135deg,#3c3c3c,#7a6e64 55%,#2a2a2a)"></div>
  <div class="date"><svg width="14" height="14" viewBox="0 0 14 14" fill="none" stroke="#f7902f" stroke-width="1.4"><rect x="1" y="2" width="12" height="11"/><path d="M1 5h12M4 0v3M10 0v3"/></svg>Jun 20, 2023</div>
  <h3>Lorem ipsum dolor sit amet, con secte tur adipiscing elit</h3>
  <a class="more" href="#">READ MORE</a>
</article>
<article class="abs post" style="left:768px">
  <div class="img" role="img" aria-label="Legal team standing in a library office" style="background:linear-gradient(135deg,#4a3a30,#8a7464 50%,#2e2622)"></div>
  <div class="date"><svg width="14" height="14" viewBox="0 0 14 14" fill="none" stroke="#f7902f" stroke-width="1.4"><rect x="1" y="2" width="12" height="11"/><path d="M1 5h12M4 0v3M10 0v3"/></svg>Nov 15, 2023</div>
  <h3>Lorem ipsum dolor sit amet, con secte tur adipiscing elit</h3>
  <a class="more" href="#">READ MORE</a>
</article>
<a class="abs btn" href="#" style="left:518px;top:3601px;width:162px;height:51px;font-size:15px">View More</a>

<!-- contact -->
<div class="abs dark-band"></div>
<div class="abs contact-box"></div>
<div class="abs eyebrow" style="left:137px;width:520px;text-align:center;top:3818px">Get In Touch</div>
<h2 class="abs" style="left:137px;width:520px;text-align:center;top:3844px;font-size:40px;font-weight:600">Contact Us</h2>
<div class="abs field" style="left:200px;top:3930px;width:210px"><svg width="12" height="12" viewBox="0 0 12 12"><circle cx="6" cy="3.5" r="3" fill="#333"/><path d="M0 12c0-4 3-5 6-5s6 1 6 5z" fill="#333"/></svg>Your Name</div>
<div class="abs field" style="left:410px;top:3930px;width:200px"><svg width="13" height="10" viewBox="0 0 13 10"><rect width="13" height="10" fill="#333"/><path d="M0 1l6.5 5L13 1" fill="none" stroke="#fde8d3"/></svg>E-Mail</div>
<div class="abs field" style="left:200px;top:4003px;width:210px"><svg width="10" height="14" viewBox="0 0 10 14"><rect x="1" y="0.5" width="8" height="13" rx="1.5" fill="none" stroke="#333"/></svg>Phone Number</div>
<div class="abs field" style="left:410px;top:4003px;width:200px"><svg width="10" height="14" viewBox="0 0 10 14"><path d="M5 0a5 5 0 015 5c0 4-5 9-5 9S0 9 0 5a5 5 0 015-5z" fill="#333"/><circle cx="5" cy="5" r="2" fill="#fde8d3"/></svg>Address</div>
<div class="abs field" style="left:196px;top:4074px;width:414px"><svg width="12" height="12" viewBox="0 0 12 12"><circle cx="6" cy="6" r="6" fill="#333"/><path d="M3 6h6" stroke="#fde8d3"/></svg>Message</div>
<a class="abs btn" href="#" style="left:318px;top:4147px;width:175px;height:50px;font-size:15px">Submit Now</a>
<div class="abs contact-frame"></div>
<div class="abs contact-photo" role="img" aria-label="Bronze gavel resting beside coins on a white desk"></div>

<!-- footer -->
<div class="abs foot-logo">
  <span class="brand-mark"></span>
  <div>
    <div class="brand-name">Morillaqua Corvell</div>
    <div class="brand-tag">Bilingual Legal Practice · Sydney</div>
  </div>
</div>
<div class="abs social"><span></span><span></span><span></span><span></span></div>

<div class="abs" style="left:594px;top:4322px">
  <div class="foot-h">Quik Links</div>
  <ul class="qlinks" style="margin-top:20px">
    <li>Home</li><li>About Us</li><li>Our Services</li><li>Download</li><li>Contact Us</li>
  </ul>
</div>
<div class="abs" style="left:828px;top:4324px">
  <div class="foot-h">Contact Us</div>
  <div class="c-item" style="margin-top:22px"><span class="c-icon"><svg width="12" height="12" viewBox="0 0 24 24"><path fill="#fff" d="M6.6 10.8a15 15 0 006.6 6.6l2.2-2.2c.3-.3.7-.4 1-.2 1.1.4 2.3.6 3.6.6.6 0 1 .4 1 1V20c0 .6-.4 1-1 1A17 17 0 013 4c0-.6.4-1 1-1h3.5c.6 0 1 .4 1 1 0 1.3.2 2.5.6 3.6.1.3 0 .7-.2 1z"/></svg></span><div>CALL US<br>(+612) 9555 0142</div></div>
  <div class="c-item" style="margin-top:16px"><span class="c-icon"><svg width="12" height="10" viewBox="0 0 12 10"><path d="M0 1l6 5 6-5" fill="none" stroke="#fff" stroke-width="1.5"/><rect x=".5" y=".5" width="11" height="9" fill="none" stroke="#fff"/></svg></span><div>EMAIL US<br>elise@corvell.com.au</div></div>
  <div class="c-item" style="margin-top:16px"><span class="c-icon"><svg width="10" height="13" viewBox="0 0 10 14"><path d="M5 0a5 5 0 015 5c0 4-5 9-5 9S0 9 0 5a5 5 0 015-5z" fill="#fff"/><circle cx="5" cy="5" r="2" fill="#f7902f"/></svg></span><div>Level 4, 28 Harbour Lane<br>Sydney, NSW 2000<br>Australia</div></div>
</div>
<div class="abs copy-line"></div>
<div class="abs copyright">Copyright © 2024 All Rights Reserved By Companyname</div>

</body>
</html>
```